Looking for a Lumora Book Cover

My book has been online for a while and I am now looking for a professional cover for it as it has been very well received.

You can view the book here and all the details about it:

https://www.pagevaultshop.example/dp/X7Q2KRMTPL#readerNotes

Not sure what I am looking for as a design, just open to your ideas.

I want something different that will stand out please.

Thanks
Owen

```html
<!DOCTYPE html>
<html lang="en">
<head>
<meta charset="utf-8">
<title>Roots and Resilience – Book Cover</title>
<link rel="stylesheet" href="https://fonts.googleapis.com/css2?family=Bebas+Neue&family=Caveat+Brush&family=Encode+Sans+Condensed:wght@500&family=Oswald:wght@600&display=swap">
<style>
  :root {
    --backdrop: #e4e4e4;
    --ink-black: #070707;
    --title-white: #e9e9e9;
    --accent-gold: #f4b73a;
    --paper: #dcdad4;
    --paper-light: #ecebe7;
    --map-beige: #c9c2b4;
    --sky-blue: #6f7f93;
    --sunset: #e08a2c;
    --script-ink: #111111;
  }
  * { margin: 0; padding: 0; box-sizing: border-box; }
  html, body {
    width: 1200px; height: 939px; overflow: hidden;
    background: var(--backdrop);
  }
  .canvas { position: relative; width: 1200px; height: 939px; }
  .book-cover {
    position: absolute; left: 325px; top: 30px;
    width: 550px; height: 880px;
    background: var(--ink-black);
    overflow: hidden;
    box-shadow: 0 14px 30px rgba(0,0,0,0.25);
  }
  .cover-photo {
    position: absolute; left: 0; top: 0; width: 550px; height: 350px;
    background:
      linear-gradient(180deg, rgba(0,0,0,0) 55%, rgba(40,25,15,0.55) 100%),
      linear-gradient(90deg, var(--sky-blue) 0%, #a99f8c 18%, var(--sunset) 26%, #6d5a50 40%, #7b6a6a 60%, var(--map-beige) 85%, #bdb6a8 100%);
  }
  .torn-edges { position: absolute; left: 0; top: 0; width: 550px; height: 880px; }
  .title-block {
    position: absolute; left: 0; top: 0; width: 550px; height: 560px;
    font-family: "Bebas Neue", sans-serif; font-weight: 400; color: var(--title-white);
    line-height: 1; white-space: nowrap;
  }
  .title-block span { position: absolute; left: 140px; }
  .title-roots { top: 346px; font-size: 107px; letter-spacing: 0; }
  .title-and {
    left: 354px !important; top: 400px;
    font-size: 50px; color: var(--accent-gold); letter-spacing: 0;
  }
  .title-resilience {
    top: 440px; font-size: 82px; letter-spacing: 0;
    transform: scaleX(0.93); transform-origin: left top;
  }
  .subtitle-strip {
    position: absolute; left: 84px; top: 552px; width: 403px; height: 112px;
    background: linear-gradient(180deg, var(--paper-light), var(--paper));
    transform: rotate(-0.4deg);
    box-shadow: 0 2px 4px rgba(0,0,0,0.35);
  }
  .subtitle {
    position: absolute; left: 56px; top: 14px;
    font-family: "Caveat Brush", cursive; font-size: 36px; line-height: 42px;
    color: var(--script-ink); white-space: nowrap;
  }
  .subtitle span { display: block; }
  .tagline {
    position: absolute; left: 77px; top: 675px;
    font-family: "Encode Sans Condensed", sans-serif; font-weight: 500;
    font-size: 24px; line-height: 31px; letter-spacing: 0.3px;
    color: #f1f1f1; white-space: nowrap;
  }
  .tagline em { font-style: normal; color: var(--accent-gold); }
  .author {
    position: absolute; left: 0; top: 782px; width: 550px;
    text-align: center;
    font-family: "Oswald", sans-serif; font-weight: 600;
    font-size: 40px; letter-spacing: 1px; color: #ffffff;
    transform: scaleX(0.86);
  }
</style>
</head>
<body>
<main class="canvas">
  <article class="book-cover">
    <div class="cover-photo" role="img" aria-label="Collage of a sunset sky with silhouetted figures, two raised hands with a linked finger and a painted symbol, archival portrait photographs, over a vintage map of Africa"></div>

    <svg class="torn-edges" viewBox="0 0 550 880" aria-hidden="true">
      <polygon fill="var(--ink-black)" points="0,338 30,333 58,340 90,331 120,337 150,330 185,339 215,332 250,336 290,329 330,338 370,332 400,337 440,331 470,336 510,330 550,334 550,560 0,560"/>
      <polygon fill="var(--paper-light)" points="437,338 470,336 500,341 530,337 550,339 550,545 520,548 490,542 460,547 437,543"/>
      <polygon fill="var(--map-beige)" points="0,540 25,535 55,543 90,537 120,544 160,538 200,545 240,536 280,542 330,537 380,544 420,538 470,543 510,536 550,541 550,622 510,617 470,624 420,618 370,625 320,619 270,626 220,619 170,624 120,618 70,625 30,619 0,623"/>
    </svg>

    <h1 class="title-block">
      <span class="title-roots">Roots</span>
      <span class="title-and">And</span>
      <span class="title-resilience">Resilience</span>
    </h1>

    <div class="subtitle-strip">
      <p class="subtitle"><span>A Celebration of Culture,</span><span>Struggle and Achievement</span></p>
    </div>

    <p class="tagline">The <em>History</em>, Resistance and <em>Excellence</em><br>of Black People <em>in Africa</em> and the Diaspora</p>

    <p class="author">DESMOND ASHWORTH</p>
  </article>
</main>
</body>
</html>
```